Newspaper Ad for Front page strip

Kestrel Quick Credit is a micro lender operating in the Caribbean. This ad is for our Trinidad and Tobago location.
Would like to design a catchy banner ad for the front page of a daily newspaper. The ad should capture 1) that we offer unsecured loans up to $40,000. 2) customer can apply online or over the phone 3) that the process is quick.
We have included the a snapshot of our Instagram posts as well as the newspaper location and size of the ad.
We have booked this ad spot for the year so the more engaging we can make it the better. Maybe we can do a series of ads or weekly storyline . Let’s be creative.
https://www.instagram.com/kestrelquickcredit/
www.kestrelquick credit.example
Target Market(s)
Mass population.
Industry/Entity Type
Banking
Look and feel

```html
<!DOCTYPE html>
<html lang="en">
<head>
<meta charset="utf-8">
<title>Kestrel Quick Credit – Unsecured Loans</title>
<link rel="stylesheet" href="https://fonts.googleapis.com/css2?family=Montserrat:wght@400;500;700;800&display=swap">
<style>
  :root {
    --green: #0f9748;
    --red: #ec2f33;
    --ink: #111111;
    --grey: #4a4a4a;
    --paper: #fbfbfb;
  }
  html, body { margin: 0; padding: 0; overflow: hidden; }
  body { width: 927px; height: 1200px; background: var(--paper); font-family: 'Montserrat', Arial, sans-serif; }
  .ad { position: relative; width: 927px; height: 1200px; overflow: hidden; background: var(--paper); }

  .hero-photo {
    position: absolute; left: 0; top: 170px; width: 927px; height: 860px;
    background: linear-gradient(100deg, #9a6a4c 0%, #c09a80 22%, #e2d6cc 45%, #f1eeea 62%, #f6f5f3 100%);
  }
  .hero-fade-top { position: absolute; left: 0; top: 170px; width: 927px; height: 160px; background: linear-gradient(180deg, var(--paper), rgba(251,251,251,0)); }
  .hero-fade-bottom { position: absolute; left: 0; top: 1030px; width: 927px; height: 170px; background: linear-gradient(180deg, #f2f1ef, var(--paper) 60%); }

  .corner { position: absolute; right: 0; top: 0; }

  .brand { position: absolute; left: 142px; top: 114px; display: flex; align-items: center; gap: 14px; }
  .brand-mark { width: 32px; height: 32px; background: var(--red); }
  .brand-name { font-weight: 800; font-size: 35px; color: var(--green); letter-spacing: -0.5px; }

  .offer { position: absolute; right: 69px; top: 282px; text-align: right; font-weight: 800; line-height: 1; }
  .offer-lead { font-size: 35px; color: var(--ink); }
  .offer-type { font-size: 50px; color: var(--red); margin-top: 0; }
  .offer-loans { font-size: 44px; color: var(--red); margin-top: -2px; }
  .offer-upto { font-size: 20px; color: var(--ink); margin-left: 8px; }
  .offer-amount { font-size: 58px; color: var(--green); margin-top: 2px; }

  .apply { position: absolute; right: 178px; top: 520px; text-align: right; font-weight: 800; font-size: 24px; line-height: 31px; color: var(--ink); }
  .apply-icon { position: absolute; left: 774px; top: 518px; }

  .benefits { position: absolute; left: 344px; top: 976px; width: 583px; height: 54px; display: flex; }
  .benefit { display: flex; align-items: center; justify-content: center; color: #fff; font-weight: 800; font-size: 35px; }
  .benefit--green { background: var(--green); }
  .benefit--red { background: var(--red); }
  .benefit--quick { width: 188px; }
  .benefit--easy { width: 183px; }
  .benefit--simple { width: 212px; }

  .contact { position: absolute; left: 91px; top: 1090px; font-size: 30px; font-weight: 500; color: var(--grey); line-height: 36px; }
  .contact-row { display: flex; align-items: center; gap: 18px; }
  .contact-row svg { width: 31px; flex: none; }

  .tagline { position: absolute; right: 65px; top: 1126px; font-size: 28px; color: var(--grey); }
  .tagline strong { color: var(--red); font-weight: 800; }
</style>
</head>
<body>
<div class="ad">
  <div class="hero-photo" role="img" aria-label="Photo of a smiling couple on a sofa looking at a smartphone together"></div>
  <div class="hero-fade-top"></div>
  <div class="hero-fade-bottom"></div>

  <svg class="corner" width="262" height="240" viewBox="0 0 262 240" aria-hidden="true">
    <polygon points="0,0 262,0 262,240" fill="#0f9748"/>
    <polygon points="128,0 262,0 262,240" fill="#ec2f33"/>
  </svg>

  <div class="brand">
    <span class="brand-mark"></span>
    <span class="brand-name">Kestrel Quick Credit</span>
  </div>

  <div class="offer">
    <div class="offer-lead">WE OFFER</div>
    <div class="offer-type">UNSECURED</div>
    <div class="offer-loans">LOANS<span class="offer-upto">UP TO</span></div>
    <div class="offer-amount">$40,000</div>
  </div>

  <div class="apply">CAN APPLY<br>ONLINE OR<br>OVER THE<br>PHONE</div>
  <svg class="apply-icon" width="94" height="124" viewBox="0 0 94 124" aria-hidden="true">
    <rect x="4" y="4" width="70" height="116" rx="9" fill="none" stroke="#ec2f33" stroke-width="7"/>
    <circle cx="39" cy="111" r="3.5" fill="#ec2f33"/>
    <path d="M73 50 A30 30 0 1 1 64 38" fill="none" stroke="#0f9748" stroke-width="8" stroke-linecap="round"/>
    <path d="M29 60 L43 74 L88 30" fill="none" stroke="#0f9748" stroke-width="9" stroke-linecap="round" stroke-linejoin="round"/>
  </svg>

  <div class="benefits">
    <div class="benefit benefit--green benefit--quick">QUICK</div>
    <div class="benefit benefit--red benefit--easy">EASY</div>
    <div class="benefit benefit--green benefit--simple">SIMPLE</div>
  </div>

  <div class="contact">
    <div class="contact-row">
      <svg viewBox="0 0 24 24" aria-hidden="true"><path fill="#ec2f33" d="M6.6 10.8a15.1 15.1 0 0 0 6.6 6.6l2.2-2.2a1 1 0 0 1 1-.25 11.4 11.4 0 0 0 3.6.57 1 1 0 0 1 1 1V20a1 1 0 0 1-1 1A17 17 0 0 1 3 4a1 1 0 0 1 1-1h3.5a1 1 0 0 1 1 1c0 1.25.2 2.45.57 3.6a1 1 0 0 1-.25 1z"/></svg>
      <span>800-KQCR (5727)</span>
    </div>
    <div class="contact-row">
      <svg viewBox="0 0 24 24" aria-hidden="true"><path fill="#ec2f33" d="M2 5h20v2.2l-10 6.3L2 7.2z M2 9.6l10 6.3 10-6.3V19H2z"/></svg>
      <span>info@kqcredit.example</span>
    </div>
  </div>

  <div class="tagline">The Choice is <strong>Clear!</strong></div>
</div>
</body>
</html>
```